Adult Coloring Book Cover Design

We need a cover created for our New Coloring book.
The title needs to be clear and visible on the front of book. Preferable easy to read when the cover is minimized to about 2 inches on screen. The Full title of the book is:
Morning Meadow Coloring Book: The Gentle Grown-Up Coloring Book for Quiet Hearts Everywhere

This is a Religious Based coloring book. Attached are some images from inside the book, feel free to add them to the cover design. We like color!
Looking for something that is attention grabbing but not too over the top.
front cover is 8.5in width and 11in length. I will need all PSD files in order to make any necessary changes once awarded.

```html
<!DOCTYPE html>
<html lang="en">
<head>
<meta charset="utf-8">
<title>Morning Meadow Coloring Book – Cover</title>
<link href="https://fonts.googleapis.com/css2?family=Oswald:wght@500;700&display=swap" rel="stylesheet">
<style>
  :root {
    --stage: #7f9ca6;
    --cover: #ffffff;
    --ink: #111111;
    --red: #e0323c;
    --orange: #f39a1e;
    --yellow: #f7d23a;
    --blue: #2f7fd0;
    --purple: #7a3cc2;
    --magenta: #d23a8c;
    --skin: #e9b79a;
  }
  * { margin: 0; padding: 0; box-sizing: border-box; }
  html, body {
    width: 1200px; height: 783px; overflow: hidden;
    background: var(--stage);
  }
  .canvas {
    position: relative; width: 1200px; height: 783px;
    display: flex; align-items: center; justify-content: center;
  }
  .cover {
    position: relative; width: 540px; height: 699px;
    background: var(--cover);
    box-shadow: 0 6px 18px rgba(0,0,0,0.18);
  }
  .pattern-field {
    position: absolute; inset: 14px 14px 14px 14px;
    border: 3px solid var(--ink);
    border-radius: 6px;
    overflow: hidden;
    background:
      radial-gradient(circle at 20% 15%, var(--red) 0 14%, transparent 30%),
      radial-gradient(circle at 80% 10%, var(--red) 0 12%, transparent 28%),
      radial-gradient(circle at 90% 45%, var(--yellow) 0 10%, transparent 26%),
      radial-gradient(circle at 10% 55%, var(--purple) 0 10%, transparent 28%),
      radial-gradient(circle at 15% 85%, var(--blue) 0 10%, transparent 30%),
      linear-gradient(160deg, var(--blue) 0%, var(--orange) 30%, var(--yellow) 45%, var(--magenta) 62%, var(--red) 75%, #f3eef3 92%);
  }
  .title-panel {
    position: absolute; left: 19%; top: 17%; width: 52%; height: 52%;
    background: var(--cover);
    border: 3px solid var(--ink);
    border-radius: 26px;
    display: flex; flex-direction: column; align-items: center; justify-content: center;
    padding: 0 22px 40px 40px;
    text-align: center;
  }
  .book-title {
    font-family: "Oswald", sans-serif;
    font-weight: 700;
    font-size: 31px;
    line-height: 1.12;
    color: var(--ink);
    text-transform: uppercase;
    letter-spacing: 0.5px;
  }
  .book-subtitle {
    margin-top: 18px;
    font-family: "Oswald", sans-serif;
    font-weight: 500;
    font-size: 15.5px;
    line-height: 1.55;
    color: var(--ink);
    text-transform: uppercase;
    letter-spacing: 0.6px;
  }
  .hand-illustration {
    position: absolute; left: 55%; top: 57%; width: 25%; height: 22%;
    border-radius: 40% 30% 20% 45%;
    background: linear-gradient(135deg, var(--red) 0%, var(--skin) 40%, var(--blue) 75%, var(--purple) 100%);
  }
</style>
</head>
<body>
  <main class="canvas">
    <article class="cover">
      <div class="pattern-field" role="img" aria-label="Colorful hand-drawn doodle pattern of swirls in red, orange, yellow, blue and purple"></div>
      <section class="title-panel">
        <h1 class="book-title">Morning Meadow<br>Coloring Book:</h1>
        <p class="book-subtitle">The Gentle Grown-Up<br>Coloring Book for Quiet<br>Hearts Everywhere</p>
      </section>
      <div class="hand-illustration" role="img" aria-label="Rainbow-painted hand holding a colored pencil"></div>
    </article>
  </main>
</body>
</html>
```